rhyming dictionary website (easy)

i need a web design for my new website which for now runs on my own self made design (i am a programmer so it sucks) you can find it at http://www.lumaquill.com

i would like a nicer design that will not cause visitors to flee in disgust.

Target Market(s)

people who search for rhymes, poets, rappers, and normal birthday greeting people

Requirements
Must have
• this is what it needs to have:

1. main page which is simple and must emphasize on the search bar.

2. search result page that will emphasize on the rhyming words and make them clear and important, it also needs to be separable like in the current "design".
it also need to have a good placement of ads, not too intrusive, not too unnoticeable

3. a general page with no real content that i can fill with anything later.
Nice to have
• also the design could combine the already exist logo that you can see on the website, i added it in the uploaded files, along with its psd.

p.s:
other design i liked that you can inspire yourself from
http://www.zelvoro.com/RhymingDictionary/hello.html

```html
<!DOCTYPE html>
<html lang="en">
<head>
<meta charset="utf-8">
<title>LumaQuill – Rhymes of design</title>
<link rel="stylesheet" href="https://fonts.googleapis.com/css2?family=Roboto+Condensed:ital,wght@0,300;0,400;0,700;1,300;1,400&display=swap">
<style>
  :root {
    --page-bg: #ffffff;
    --header-bg: #ececec;
    --band-top: #4b4b4b;
    --band-bottom: #3a3a3a;
    --ink: #333333;
    --ink-soft: #444444;
    --muted: #cfcfcf;
    --link: #5fc3ec;
    --green: #6cc05a;
    --green-dark: #55a444;
    --panel: #f4f4f4;
    --row-alt: #e6e6e6;
    --rule: #222222;
    --ad-bg: #e6e6e6;
    --ad-border: #c8c8c8;
    --ad-text: #a8a8a8;
    --field-bg: #f6f6f6;
    --field-border: #d2d2d2;
    --brand-mark: #6cc05a;
  }
  * { box-sizing: border-box; margin: 0; padding: 0; }
  html, body { width: 1200px; height: 1125px; overflow: hidden; }
  body {
    position: relative;
    background: var(--page-bg);
    font-family: "Roboto Condensed", "Arial Narrow", sans-serif;
    color: var(--ink);
  }

  .site-header { position: absolute; left: 0; top: 0; width: 1200px; height: 112px; background: var(--header-bg); }
  .brand { position: absolute; left: 189px; top: 38px; display: flex; align-items: center; gap: 20px; }
  .brand-mark { width: 30px; height: 30px; background: var(--brand-mark); }
  .brand-name { font-size: 23px; font-weight: 700; line-height: 1; color: var(--ink); }
  .brand-tagline { font-size: 13px; font-weight: 400; color: var(--ink); margin-top: 2px; }

  .search-form { position: absolute; left: 560px; top: 31px; display: flex; gap: 16px; }
  .search-field {
    width: 333px; height: 49px; border: 1px solid var(--field-border); border-radius: 4px;
    background: var(--field-bg); box-shadow: inset 0 2px 4px rgba(0,0,0,.08);
    font: italic 300 16px "Roboto Condensed", sans-serif; color: #a0a0a0;
    padding: 0 19px; display: flex; align-items: center;
  }
  .search-button {
    width: 125px; height: 50px; border-radius: 3px; background: var(--green);
    border-bottom: 4px solid var(--green-dark);
    color: #fff; font: 700 16px "Roboto Condensed", sans-serif;
    display: flex; align-items: center; justify-content: center;
    text-shadow: 0 1px 1px rgba(0,0,0,.3);
  }

  .latest-band {
    position: absolute; left: 0; top: 112px; width: 1200px; height: 92px;
    background: linear-gradient(var(--band-top), var(--band-bottom));
    display: flex; align-items: center; padding-left: 189px; gap: 22px;
  }
  .latest-label { color: #fff; font-size: 16px; font-weight: 700; margin-right: 6px; }
  .latest-link { color: var(--link); font-size: 16px; font-style: italic; text-decoration: underline; }

  .result-title { position: absolute; left: 0; top: 232px; width: 1200px; text-align: center; font-size: 45px; font-weight: 700; color: var(--ink); }
  .result-subtitle { position: absolute; left: 0; top: 307px; width: 1200px; text-align: center; font-size: 23px; font-weight: 400; color: var(--muted); }

  .rhyme-panel { position: absolute; left: 305px; top: 378px; width: 591px; height: 309px; background: var(--panel); border-radius: 3px; padding: 0 19px 0 20px; }
  .rhyme-row {
    display: grid; grid-template-columns: 119px 105px 125px 120px auto; align-items: center;
    padding-left: 10px; font-size: 29px; font-weight: 300; font-style: italic; color: var(--ink-soft);
  }
  .rhyme-row--top { height: 72px; border-bottom: 1px solid var(--rule); margin: 0 2px; padding-left: 8px; }
  .rhyme-row--shaded { height: 56px; background: var(--row-alt); border-radius: 3px; margin-top: 15px; }
  .rhyme-row--ruled { height: 67px; border-bottom: 1px solid var(--rule); margin: 0 2px; padding-left: 8px; }

  .ad-slot {
    position: absolute; top: 715px; width: 281px; height: 235px;
    background: var(--ad-bg); border: 1px solid var(--ad-border);
    display: flex; align-items: center; justify-content: center;
    color: var(--ad-text); font-size: 16px; font-style: italic; font-weight: 300;
  }
  .ad-slot--left { left: 305px; }
  .ad-slot--right { left: 615px; }

  .site-footer { position: absolute; left: 0; top: 1030px; width: 1200px; text-align: center; font-size: 17px; font-weight: 300; line-height: 28px; color: var(--ink); }
</style>
</head>
<body>
  <header class="site-header">
    <div class="brand">
      <span class="brand-mark"></span>
      <div>
        <div class="brand-name">LumaQuill</div>
        <div class="brand-tagline">- Your online source for rhymes</div>
      </div>
    </div>
    <div class="search-form">
      <div class="search-field">DESIGN</div>
      <div class="search-button">FIND OUT</div>
    </div>
  </header>

  <nav class="latest-band">
    <span class="latest-label">LATEST SEARCHES:</span>
    <span class="latest-link">Hello</span>
    <span class="latest-link">Sex</span>
    <span class="latest-link">Dead</span>
    <span class="latest-link">more</span>
    <span class="latest-link">throne</span>
  </nav>

  <h1 class="result-title">DESIGN</h1>
  <p class="result-subtitle">One- and two-syllable End Rhymes of design:</p>

  <section class="rhyme-panel">
    <div class="rhyme-row rhyme-row--top"><span>airline</span><span>align</span><span>assign</span><span>define</span><span>divine</span></div>
    <div class="rhyme-row rhyme-row--shaded"><span>airline</span><span>align</span><span>assign</span><span>define</span><span>divine</span></div>
    <div class="rhyme-row rhyme-row--ruled"><span>airline</span><span>align</span><span>assign</span><span>define</span><span>divine</span></div>
    <div class="rhyme-row rhyme-row--shaded"><span>airline</span><span>align</span><span>assign</span><span>define</span><span>divine</span></div>
  </section>

  <div class="ad-slot ad-slot--left">300x250</div>
  <div class="ad-slot ad-slot--right">300x250</div>

  <footer class="site-footer">
    <p>All rights are allright</p>
    <p>They are reserved as they well deserved.</p>
  </footer>
</body>
</html>
```